Self-Serve Brazilian Buffet and BBQ sold by the pound needs a business card

For CEO -Lucia Fernanda Moura Blake
Owner/President - Marco Tiago Moura

Target Market(s)

Customers and

Industry/Entity Type

Business

Contact Information for Business Card

Lucia Fernanda Pinto Moura Blake
CEO of Terra Sol Churrasco
Brazilian BBQ Buffet sold by the pound

Requirements
Must have
• 5218 West Orchard Ave.
• Ste. K
• Santa Ana, CA 92781
• Phone : 714382-0157
• terrasolchurrasco@mailbox-example.com

```html
<!DOCTYPE html>
<html lang="en">
<head>
<meta charset="utf-8">
<title>Terra Sol Churrasco – Business Card</title>
<link href="https://fonts.googleapis.com/css2?family=Arimo:wght@400&display=swap" rel="stylesheet">
<style>
  :root {
    --bg: #e6e3df;
    --card: #ffffff;
    --card-shade: #ececec;
    --red: #b3301e;
    --red-dark: #8e2213;
    --ink: #1c1c1c;
    --meat-dark: #3f1e14;
    --meat-mid: #6b3424;
    --meat-light: #8a4a33;
  }
  html, body {
    margin: 0;
    width: 1200px;
    height: 892px;
    overflow: hidden;
    background: var(--bg);
  }
  .card {
    position: absolute;
    left: 75px;
    top: 146px;
    width: 1050px;
    height: 600px;
    background: linear-gradient(180deg, var(--card) 0%, var(--card) 55%, var(--card-shade) 100%);
    box-shadow: 0 10px 30px rgba(0,0,0,0.25);
    overflow: hidden;
  }
  .food-photo {
    position: absolute;
    left: 0;
    top: 0;
    width: 520px;
    height: 600px;
  }
  .brand-name {
    position: absolute;
    left: 520px;
    top: 58px;
    width: 270px;
    text-align: center;
    font-family: "Arimo", Arial, sans-serif;
    font-weight: 400;
    font-size: 44px;
    line-height: 1.1;
    color: var(--red);
  }
  .person {
    position: absolute;
    right: 95px;
    top: 250px;
    text-align: right;
    font-family: "Arimo", Arial, sans-serif;
    color: var(--ink);
  }
  .person .name { font-size: 40px; line-height: 1.1; }
  .person .title { font-size: 22px; margin-top: 2px; }
  .divider {
    position: absolute;
    left: 560px;
    right: 95px;
    top: 352px;
    height: 2px;
    background: var(--red);
  }
  .contact {
    position: absolute;
    right: 55px;
    top: 372px;
    text-align: right;
    font-family: "Arimo", Arial, sans-serif;
    font-size: 23px;
    line-height: 31px;
    color: var(--ink);
  }
  .contact .line { display: flex; justify-content: flex-end; align-items: center; gap: 10px; }
  .contact .icon { width: 26px; height: 26px; flex: none; }
  .contact .spacer { width: 26px; flex: none; }
</style>
</head>
<body>
  <div class="card">
    <svg class="food-photo" viewBox="0 0 520 600" role="img" aria-label="Photo of grilled Brazilian barbecue short ribs topped with green onion and sesame">
      <defs>
        <radialGradient id="meatTone" cx="45%" cy="50%" r="70%">
          <stop offset="0%" stop-color="var(--meat-light)"/>
          <stop offset="55%" stop-color="var(--meat-mid)"/>
          <stop offset="100%" stop-color="var(--meat-dark)"/>
        </radialGradient>
      </defs>
      <path d="M0 0 H390 Q540 300 430 600 H0 Z" fill="url(#meatTone)"/>
      <path d="M390 0 Q540 300 430 600" fill="none" stroke="var(--red-dark)" stroke-width="20"/>
      <path d="M390 0 Q540 300 430 600" fill="none" stroke="var(--red)" stroke-width="13"/>
    </svg>

    <div class="brand-name">Terra Sol Churrasco</div>

    <div class="person">
      <div class="name">Marco Tiago Moura</div>
      <div class="title">Owner/President</div>
    </div>

    <div class="divider"></div>

    <div class="contact">
      <div class="line">714382-0157
        <svg class="icon" viewBox="0 0 26 26" aria-hidden="true">
          <rect width="26" height="26" fill="var(--ink)"/>
          <rect x="3" y="3" width="20" height="20" fill="var(--red)"/>
          <path d="M8 7 l3 0 l1 4 l-2 1 q1 3 4 4 l1 -2 l4 1 l0 3 q-9 1 -11 -11z" fill="#fff"/>
        </svg>
      </div>
      <div class="line">terrasolchurrasco@mailbox-example.com
        <svg class="icon" viewBox="0 0 26 26" aria-hidden="true">
          <rect width="26" height="26" fill="var(--ink)"/>
          <rect x="3" y="3" width="20" height="20" fill="var(--red)"/>
          <rect x="6" y="8" width="14" height="10" fill="none" stroke="#fff" stroke-width="1.6"/>
          <path d="M6 8 L13 14 L20 8" fill="none" stroke="#fff" stroke-width="1.6"/>
        </svg>
      </div>
      <div class="line">5218 West Orchard Ave. Ste. K<span class="spacer"></span></div>
      <div class="line">Santa Ana, CA 92781<span class="spacer"></span></div>
    </div>
  </div>
</body>
</html>
```